Screening Mammography flyer for patients

We need a flyer design to inform our patients of our Screening Mammography program (it's a screening Diagnostic Imaging test). Women aged 50-74 years old are eligible for this exam. We also have a convenient booking system, when a patient can call us directly. There's no doctor’s referral needed to sign up for the test.
We are also starting the RVC Scan Champion program, when select patients will help spread the word and save lives.
The flyer has to be done with a lot of pink color as it is a traditional color for Breast cancer materials, with consideration of the hospital's corporate colors (the brand book is attached).

Industry/Entity Type

Diagnostic Imaging

```html
<!DOCTYPE html>
<html lang="en">
<head>
<meta charset="utf-8">
<title>Screening Mammography Flyer</title>
<link href="https://fonts.googleapis.com/css2?family=Oswald:wght@500;700&family=Source+Sans+3:ital,wght@0,400;0,600;0,700;1,700&display=swap" rel="stylesheet">
<style>
  :root {
    --pink: #ef7aa2;
    --pink-deep: #e0327f;
    --green: #a7cf3a;
    --green-text: #78b12f;
    --teal: #16b0c2;
    --purple: #6a3f98;
    --ink: #1d1d1d;
    --grey-text: #3a3a3a;
    --page: #e8e5e2;
    --white: #ffffff;
  }
  * { box-sizing: border-box; margin: 0; padding: 0; }
  html, body { width: 1200px; height: 964px; overflow: hidden; background: var(--page); }
  body { position: relative; font-family: "Source Sans 3", Arial, sans-serif; }

  .flyer {
    position: absolute; left: 20px; top: 73px;
    width: 1160px; height: 818px;
    background: var(--white);
    box-shadow: 0 2px 10px rgba(0,0,0,.12);
  }
  .flyer-face {
    position: absolute; left: 21px; top: 19px;
    width: 1120px; height: 780px;
    overflow: hidden;
    background: linear-gradient(180deg, #ffffff 45%, #ececec 100%);
  }
  .swoosh { position: absolute; inset: 0; width: 1120px; height: 780px; }

  .headline {
    position: absolute; left: 38px; top: 30px;
    font-family: "Oswald", Impact, sans-serif; font-weight: 700;
    font-size: 98px; line-height: 1; color: var(--white);
    letter-spacing: 1px;
    text-shadow: 2px 2px 3px rgba(0,0,0,.25);
  }
  .audience {
    position: absolute; left: 38px; top: 150px;
    font-family: "Oswald", Impact, sans-serif; font-weight: 700;
    font-size: 47px; line-height: 1; color: var(--white);
    letter-spacing: .5px;
    text-shadow: 1px 1px 2px rgba(0,0,0,.2);
  }
  .web-link {
    position: absolute; left: 42px; top: 220px;
    font-weight: 700; font-size: 29px; color: var(--ink);
  }
  .photo-women {
    position: absolute; left: 18px; top: 262px;
    width: 460px; height: 518px;
    background: linear-gradient(180deg, #f3a3be 0%, #f7b6cc 45%, #5c7fae 82%, #46689a 100%);
    border-radius: 160px 160px 0 0;
  }

  .badge-early {
    position: absolute; left: 502px; top: 226px;
    width: 174px; height: 174px; border-radius: 50%;
    background: var(--white); border: 7px solid var(--pink-deep);
    display: flex; flex-direction: column; align-items: center; justify-content: center;
    font-family: "Oswald", Impact, sans-serif; font-weight: 700;
    color: var(--pink-deep); line-height: .95; text-align: center;
  }
  .badge-early .big { font-size: 31px; }
  .badge-early .small { font-size: 17px; font-weight: 500; }

  .badge-referral {
    position: absolute; left: 454px; top: 507px;
    width: 244px; height: 244px; border-radius: 50%;
    background: #e4e4e4;
    display: flex; align-items: center; justify-content: center;
  }
  .badge-referral p {
    width: 216px; height: 216px; border-radius: 50%;
    background: var(--green); color: var(--white);
    display: flex; align-items: center; justify-content: center; text-align: center;
    font-weight: 700; font-size: 25px; line-height: 1.24;
  }

  .brand {
    position: absolute; left: 783px; top: 42px; width: 302px;
  }
  .brand-name {
    display: flex; align-items: center; gap: 16px;
  }
  .brand-mark { width: 72px; height: 72px; background: var(--green); flex: none; }
  .brand-name span {
    font-weight: 700; font-size: 22px; line-height: 1.05; color: #3d3d3d; letter-spacing: 1px;
  }
  .brand-network {
    margin-top: 12px; padding-top: 8px; border-top: 2px solid var(--green);
    font-weight: 700; font-size: 14px; color: var(--green-text); letter-spacing: 1.9px;
    white-space: nowrap;
  }

  .contact { position: absolute; right: 20px; text-align: right; white-space: nowrap; }
  .book-title {
    top: 206px;
    font-family: "Oswald", Impact, sans-serif; font-weight: 500;
    font-size: 45px; line-height: 1; color: var(--purple);
    transform: scaleX(.83); transform-origin: right center;
  }
  .book-phone {
    top: 259px;
    font-family: "Oswald", Impact, sans-serif; font-weight: 500;
    font-size: 46px; line-height: 1; color: var(--green-text);
  }
  .book-phone small { font-size: 36px; }
  .same-day {
    position: absolute; left: 705px; top: 318px; width: 392px; height: 33px;
    background: var(--pink-deep); color: var(--white);
    font-weight: 700; font-size: 21px; line-height: 33px;
    text-align: right; padding-right: 8px;
  }
  .appt-label {
    top: 390px; font-weight: 700; font-style: italic; font-size: 29px; color: var(--pink-deep);
  }
  .appt-time { top: 434px; font-weight: 600; font-size: 25px; color: var(--ink); }
  .divider {
    position: absolute; left: 694px; top: 525px; width: 406px; height: 1px; background: #bdbdbd;
  }
  .program-title { top: 538px; font-weight: 700; font-size: 31px; color: var(--green-text); }
  .program-text { top: 578px; font-weight: 600; font-size: 19px; line-height: 1.5; color: var(--grey-text); }
  .imaging-title { top: 656px; font-weight: 600; font-size: 26px; line-height: 1.22; color: var(--green-text); }
  .address { top: 728px; font-weight: 600; font-size: 21px; color: var(--grey-text); }
</style>
</head>
<body>
  <main class="flyer">
    <div class="flyer-face">
      <svg class="swoosh" viewBox="0 0 1120 780" aria-hidden="true">
        <path fill="var(--green)" d="M0,0 H808 C680,110 600,260 585,420 C575,560 610,680 665,780 H0Z"/>
        <path fill="var(--teal)" d="M0,0 H734 C620,140 560,310 566,500 C572,620 612,710 696,780 H0Z"/>
        <path fill="var(--purple)" d="M0,0 H718 C600,150 545,320 552,510 C558,630 594,715 663,780 H0Z"/>
        <path fill="var(--pink)" d="M0,0 H716 C592,150 536,320 542,500 C547,620 582,710 635,780 H0Z"/>
      </svg>

      <h1 class="headline">JUST BOOK IT!</h1>
      <h2 class="audience">FOR WOMEN AGED 50-74</h2>
      <p class="web-link">www.ehhn.ca/imaging</p>

      <div class="photo-women" role="img" aria-label="Photo of three smiling women of different ages in pink tops embracing"></div>

      <div class="badge-early">
        <span class="big">EARLY</span>
        <span class="small">DETECTION</span>
        <span class="big">SAVES</span>
        <span class="big">LIVES</span>
      </div>

      <div class="badge-referral">
        <p>No doctor’s<br>referral<br>needed for your<br>Screening<br>Mammogram</p>
      </div>

      <div class="brand">
        <div class="brand-name">
          <div class="brand-mark"></div>
          <span>RIVERDALE<br>VALLEY<br>CENTRE</span>
        </div>
        <p class="brand-network">EASTSIDE HARBOUR HEALTH NETWORK</p>
      </div>

      <p class="contact book-title">TO BOOK AN APPOINTMENT</p>
      <p class="contact book-phone">555-014-2290 <small>ext 4471</small></p>
      <p class="same-day">Same Day appointments available !</p>

      <p class="contact appt-label">Your Appointment’s</p>
      <p class="contact appt-time">Date &amp; Time:</p>

      <div class="divider"></div>

      <p class="contact program-title">Ambassador Program</p>
      <p class="contact program-text">Join the RVC Scan Champion<br>Program to help save lives!</p>
      <p class="contact imaging-title">Diagnostic Imaging @<br>Riverdale Valley Centre:</p>
      <p class="contact address">410 Alder Ave. Email:&nbsp; imaging@ehhn.ca</p>
    </div>
  </main>
</body>
</html>
```